Business Card Design Project

Business Card
We are rebranding with a new logo
Industry/Entity Type
Business
Contact Information for Business Card
Dennis Marlow +61 427581962 dennis@qovo.com.au P.O. Box 872 Kelvindale QLD 4309
Requirements
Must have
- Logo

```html
<!DOCTYPE html>
<html lang="en">
<head>
<meta charset="utf-8">
<title>Qovo International – Business Card</title>
<link rel="stylesheet" href="https://fonts.googleapis.com/css2?family=Mulish:wght@800&family=Questrial&display=swap">
<style>
  :root {
    --page-bg: #5a5a5a;
    --card-white: #f7f7f7;
    --card-grey: #d4d4d4;
    --blue-light: #2aa3dc;
    --blue-mid: #1b7aa8;
    --blue-deep: #063f5e;
    --blue-edge: #0c5c86;
    --orange: #ef8a22;
    --brand-blue: #1a73a6;
    --text-light: #e4eef4;
    --ink: #1a1a1a;
  }
  html, body {
    margin: 0;
    width: 1200px;
    height: 965px;
    overflow: hidden;
    background: var(--page-bg);
  }
  .business-card {
    position: absolute;
    left: 51px;
    top: 170px;
    width: 980px;
    height: 558px;
    transform: scale(1.12);
    transform-origin: 0 0;
    border-radius: 56px;
    overflow: hidden;
    box-shadow: 0 18px 40px rgba(0,0,0,0.45);
  }
  .card-art {
    position: absolute;
    inset: 0;
    width: 980px;
    height: 558px;
  }
  .brand {
    position: absolute;
    left: 62px;
    top: 170px;
    width: 360px;
    text-align: center;
    color: var(--brand-blue);
    font-family: "Questrial", sans-serif;
  }
  .brand-name {
    display: block;
    font-size: 132px;
    line-height: 1;
    letter-spacing: 2px;
  }
  .brand-sub {
    display: block;
    margin-top: 14px;
    font-size: 31px;
    letter-spacing: 5px;
  }
  .contact {
    position: absolute;
    left: 625px;
    top: 128px;
    font-family: "Questrial", sans-serif;
    color: var(--text-light);
  }
  .contact-name {
    margin: 0 0 62px;
    font-family: "Mulish", sans-serif;
    font-weight: 800;
    font-size: 28px;
    color: var(--orange);
    letter-spacing: 0.2px;
  }
  .contact-list {
    list-style: none;
    margin: 0;
    padding: 0;
  }
  .contact-list li {
    display: flex;
    align-items: center;
    height: 28px;
    font-size: 22px;
  }
  .contact-list svg {
    width: 22px;
    height: 22px;
    margin-right: 15px;
    flex: none;
  }
  .contact-address {
    margin: 60px 0 0;
    font-size: 22px;
    line-height: 29px;
    font-style: normal;
  }
</style>
</head>
<body>
<main class="business-card">
  <svg class="card-art" viewBox="0 0 980 558" aria-hidden="true">
    <defs>
      <linearGradient id="blue-field" x1="0" y1="0" x2="1" y2="0.6">
        <stop offset="0.45" stop-color="var(--blue-light)"/>
        <stop offset="0.7" stop-color="var(--blue-mid)"/>
        <stop offset="1" stop-color="var(--blue-deep)"/>
      </linearGradient>
      <linearGradient id="white-field" x1="0" y1="0" x2="0" y2="1">
        <stop offset="0" stop-color="var(--card-white)"/>
        <stop offset="1" stop-color="var(--card-grey)"/>
      </linearGradient>
    </defs>
    <rect class="blue-field" width="980" height="558" fill="url(#blue-field)"/>
    <path class="orange-band" d="M0 0 H490 Q645 280 490 558 H0 Z" fill="var(--orange)" stroke="#fff" stroke-width="2"/>
    <path class="edge-band" d="M0 0 H440 Q640 280 480 558 H0 Z" fill="var(--blue-edge)" stroke="#fff" stroke-width="1.5"/>
    <path class="white-field" d="M0 0 H430 Q650 280 425 558 H0 Z" fill="url(#white-field)"/>
  </svg>

  <div class="brand">
    <span class="brand-name">Qovo</span>
    <span class="brand-sub">INTERNATIONAL</span>
  </div>

  <section class="contact">
    <h1 class="contact-name">Dennis Marlow</h1>
    <ul class="contact-list">
      <li>
        <svg viewBox="0 0 24 24"><path fill="var(--orange)" d="M6.6 2.5c.6-.3 1.2 0 1.5.5l2 3.4c.3.5.2 1.2-.3 1.6l-1.6 1.2c.9 2 2.6 3.8 4.6 4.8l1.3-1.6c.4-.5 1.1-.6 1.6-.3l3.4 2c.5.3.8 1 .5 1.6l-1 2.3c-.4.8-1.3 1.3-2.2 1.1C9.9 18 5.3 13.3 3.9 6.8c-.2-.9.3-1.8 1.1-2.2z"/></svg>
        +61 427581962
      </li>
      <li>
        <svg viewBox="0 0 24 24"><rect x="2" y="5" width="20" height="14" fill="var(--orange)"/><path d="M2 5l10 8 10-8M2 19l7-7M22 19l-7-7" fill="none" stroke="#fff" stroke-width="1.4"/></svg>
        dennis@qovo.com.au
      </li>
      <li>
        <svg viewBox="0 0 24 24" fill="none" stroke="var(--orange)" stroke-width="1.8"><circle cx="12" cy="12" r="9.5"/><ellipse cx="12" cy="12" rx="4" ry="9.5"/><path d="M2.5 12h19M4 7h16M4 17h16"/></svg>
        www.qovo.com.au
      </li>
    </ul>
    <address class="contact-address">P.O. Box 872 Kelvindale<br>QLD 4309</address>
  </section>
</main>
</body>
</html>
```